Marketing Flyer for Plumber Referals

8.5" x11" Layout should be landscape not portrait. Create a bold, eye-catching flyer that highlights earning potential from referrals for water damage restoration. Use high-contrast colors like blue, yellow, and white, with bold fonts and dynamic layouts. Include images of restoration work, cash, and happy clients. Emphasize key benefits like $500 minimum payouts, fast payments, and unlimited income potential. Keep instructions simple: refer a client, we handle the work, you get paid. Add a clear call-to-action and display contact details prominently. Focus on professionalism and energy.

Target Market(s)

Plumbers and Contractor 8.5" x11" Layout should be landscape not portrait.

Industry/Entity Type

General Contractor

Colors
0054AA
0677BA
7BADD7
CADEEF
E8F1F8
EB3D1F
EC4F4E
F09395
F8D3D4
FCEDEE

Requirements
Must have
• 8.5" x11" Layout should be landscape not portrait.
Nice to have

```html
<!DOCTYPE html>
<html lang="en">
<head>
<meta charset="utf-8">
<title>Referral Flyer – Water Damage Restoration</title>
<link href="https://fonts.googleapis.com/css2?family=Playfair+Display:wght@400;700&family=Roboto:wght@400;500;700;900&display=swap" rel="stylesheet">
<style>
  :root {
    --brand-blue: #0054AA;
    --deep-navy: #0D3B61;
    --accent-red: #EB3D1F;
    --ink: #1b1b1b;
    --white: #ffffff;
  }
  * { box-sizing: border-box; margin: 0; padding: 0; }
  html, body { width: 1200px; height: 1200px; overflow: hidden; background: var(--white); }
  body { position: relative; font-family: 'Roboto', Arial, sans-serif; color: var(--ink); }

  .flyer {
    position: absolute; left: 233px; width: 774px; height: 434px;
    background: var(--white); overflow: visible;
  }
  .flyer--front { top: 99px; }
  .flyer--back { top: 632px; }
  .flyer::after {
    content: ""; position: absolute; left: 10px; right: 10px; top: 434px; height: 36px;
    background: radial-gradient(ellipse at 50% 0%, rgba(0,0,0,0.22) 0%, rgba(0,0,0,0.06) 45%, rgba(0,0,0,0) 70%);
    z-index: -1;
  }
  .flyer__inner { position: absolute; inset: 0; overflow: hidden; }

  .wave { position: absolute; left: 0; top: 0; width: 774px; height: 200px; z-index: 2; }

  .headline {
    position: absolute; left: 0; right: 0; color: var(--white);
    font-family: 'Playfair Display', Georgia, serif; text-align: center; z-index: 3; line-height: 1;
    white-space: nowrap;
  }
  .headline--earn { top: 12px; font-size: 56px; font-weight: 700; letter-spacing: -0.5px; }
  .headline--sub { top: 71px; font-size: 29px; font-weight: 400; letter-spacing: 0.3px; }
  .headline--refer { top: 17px; font-size: 71px; font-weight: 700; letter-spacing: -0.5px; }
  .headline--flood { top: 93px; left: auto; right: 50px; text-align: right; font-size: 55px; font-weight: 700; }

  .photo { position: absolute; z-index: 1; }
  .photo--pipe {
    left: 370px; top: 150px; width: 220px; height: 250px;
    background: radial-gradient(ellipse at 55% 45%, #dfe2e6 0%, #c9cdd2 35%, rgba(255,255,255,0) 72%);
  }
  .photo--stairs {
    left: 0; top: 120px; width: 440px; height: 280px;
    background:
      linear-gradient(90deg, rgba(255,255,255,0) 0%, rgba(255,255,255,0) 70%, #ffffff 100%),
      linear-gradient(180deg, #c6c9cc 0%, #d8d6d0 40%, #bfc3c6 58%, #a9afb4 75%, #d6d9dc 100%);
  }

  .pitch { position: absolute; left: 20px; top: 180px; z-index: 3; font-weight: 700; font-size: 30px; line-height: 33px; white-space: nowrap; }
  .pitch__red { color: var(--accent-red); display: block; }
  .pitch__blue { color: var(--brand-blue); display: block; }

  .benefits-title { position: absolute; left: 22px; top: 262px; font-size: 21px; font-weight: 700; z-index: 3; }
  .benefits { position: absolute; left: 20px; top: 296px; list-style: none; z-index: 3; }
  .benefits li { display: flex; align-items: center; height: 22px; font-size: 11px; }
  .benefits svg { width: 13px; height: 13px; margin-right: 6px; flex: none; }
  .benefits strong { font-weight: 700; }

  .offer { position: absolute; left: 575px; top: 222px; width: 180px; z-index: 3; font-weight: 900; }
  .offer__amount { position: relative; color: var(--accent-red); font-size: 74px; line-height: 74px; letter-spacing: -1px; height: 62px; overflow: hidden; }
  .offer__min {
    position: absolute; left: 84px; top: 50px; background: var(--white); color: var(--accent-red);
    font-size: 16px; font-weight: 700; line-height: 16px; padding: 0 2px; letter-spacing: 0.3px;
  }
  .offer__pct { color: var(--brand-blue); font-size: 55px; line-height: 52px; letter-spacing: -1px; margin-top: 4px; }
  .offer__per { color: var(--brand-blue); font-size: 21px; font-weight: 900; line-height: 24px; margin-top: 2px; }

  .steps-title { position: absolute; left: 451px; top: 219px; font-size: 18px; font-weight: 500; z-index: 3; }
  .steps { position: absolute; left: 445px; top: 249px; list-style: none; z-index: 3; font-size: 11px; line-height: 17.5px; }
  .steps b { font-weight: 700; }
  .steps .step__desc { display: block; padding-left: 12px; }

  .cta-bar { position: absolute; left: 0; bottom: 0; width: 774px; height: 34px; z-index: 4; }
  .cta-bar svg { position: absolute; inset: 0; }
  .cta-bar span {
    position: absolute; top: 0; height: 34px; line-height: 34px; color: var(--white);
    font-weight: 700; font-size: 17px; transform: translateX(-50%); white-space: nowrap;
  }
</style>
</head>
<body>

<section class="flyer flyer--front">
  <div class="flyer__inner">
    <svg class="wave" viewBox="0 0 774 200" aria-hidden="true">
      <path fill="var(--brand-blue)" d="M0 0 H774 V151 C700 175 620 182 579 176 C450 160 330 125 229 127 C130 129 50 150 0 169 Z"/>
      <path fill="var(--accent-red)" d="M80 152 C160 134 230 132 300 137 C420 147 500 181 579 184 C660 187 725 176 774 166 V151 C700 175 620 182 579 176 C470 168 350 128 229 130 C160 131 110 141 80 152 Z"/>
    </svg>
    <h1 class="headline headline--earn">EARN UNLIMITED CASH</h1>
    <p class="headline headline--sub">GET PAID TO REFER A FLOOD</p>

    <div class="photo photo--pipe" role="img" aria-label="White drain pipe with leaking water"></div>

    <h2 class="pitch"><span class="pitch__red">Partner with the #1 Water Damage</span><span class="pitch__blue">Restoration Team</span></h2>

    <h3 class="benefits-title">Why Partner with Us?</h3>
    <ul class="benefits">
      <li><svg viewBox="0 0 14 14"><rect x="1" y="2" width="10" height="10" rx="1.5" fill="none" stroke="var(--brand-blue)" stroke-width="1.6"/><path d="M3.5 6.5 L6 9 L12.5 2" fill="none" stroke="var(--brand-blue)" stroke-width="2"/></svg><span><strong>Guaranteed Payout</strong> : Minimum $500 or 10% of the invoice, paid fast.</span></li>
      <li><svg viewBox="0 0 14 14"><rect x="1" y="2" width="10" height="10" rx="1.5" fill="none" stroke="var(--brand-blue)" stroke-width="1.6"/><path d="M3.5 6.5 L6 9 L12.5 2" fill="none" stroke="var(--brand-blue)" stroke-width="2"/></svg><span><strong>Free Evaluations</strong> : We assess damage and process insurance claims for your clients.</span></li>
      <li><svg viewBox="0 0 14 14"><rect x="1" y="2" width="10" height="10" rx="1.5" fill="none" stroke="var(--brand-blue)" stroke-width="1.6"/><path d="M3.5 6.5 L6 9 L12.5 2" fill="none" stroke="var(--brand-blue)" stroke-width="2"/></svg><span><strong>Industry Leaders</strong> : Certified experts with 24/7 rapid response.</span></li>
      <li><svg viewBox="0 0 14 14"><rect x="1" y="2" width="10" height="10" rx="1.5" fill="none" stroke="var(--brand-blue)" stroke-width="1.6"/><path d="M3.5 6.5 L6 9 L12.5 2" fill="none" stroke="var(--brand-blue)" stroke-width="2"/></svg><span><strong>Affordable Solutions</strong>: Lowest out-of-pocket costs for your customers.</span></li>
    </ul>

    <div class="offer">
      <div class="offer__amount">$500</div>
      <span class="offer__min">MINIMUM</span>
      <div class="offer__pct">OR10%</div>
      <div class="offer__per">PER REFERRAL!</div>
    </div>

    <div class="cta-bar">
      <svg viewBox="0 0 774 34" aria-hidden="true">
        <rect width="774" height="34" fill="var(--brand-blue)"/>
        <polygon points="276,0 482,0 444,34 238,34" fill="var(--deep-navy)"/>
      </svg>
      <span style="left:93px">Send Referrals</span>
      <span style="left:354px">Get Paid</span>
      <span style="left:624px">Grow Your Business</span>
    </div>
  </div>
</section>

<section class="flyer flyer--back">
  <div class="flyer__inner">
    <div class="photo photo--stairs" role="img" aria-label="Flooded hallway with staircase standing in water"></div>
    <svg class="wave" viewBox="0 0 774 200" aria-hidden="true">
      <path fill="var(--brand-blue)" d="M0 0 H774 V149 C700 172 610 180 540 172 C430 158 360 132 292 130 C170 128 70 146 0 168 Z"/>
      <path fill="var(--accent-red)" d="M0 168 C70 144 170 124 292 128 C360 130 430 152 540 170 C610 181 700 174 774 149 V162 C705 186 620 192 540 184 C430 170 360 140 292 136 C170 132 70 150 0 171 Z"/>
    </svg>
    <h1 class="headline headline--refer">GET PAID TO REFER</h1>
    <p class="headline headline--flood">A FLOOD</p>

    <h3 class="steps-title">How It Works</h3>
    <ol class="steps">
      <li><b>1. Refer Flood, Water and Mold Damage</b><span class="step__desc">Call, book online, or text us directly.</span></li>
      <li><b>2. We Take Care of Everything</b><span class="step__desc">Free evaluations, insurance claims, and professional service.</span></li>
      <li><b>3. Get Paid Fast</b><span class="step__desc">$500 minimum or 10% of the invoice within 48 hours<br>of final payment.</span></li>
    </ol>

    <div class="cta-bar">
      <svg viewBox="0 0 774 34" aria-hidden="true">
        <rect width="774" height="34" fill="var(--brand-blue)"/>
        <polygon points="332,0 523,0 486,34 311,34" fill="var(--deep-navy)"/>
      </svg>
      <span style="left:146px">Call Text or Book On-line</span>
      <span style="left:412px">555-014-2277</span>
      <span style="left:649px">HarborlineRestore.com</span>
    </div>
  </div>
</section>

</body>
</html>
```